Postcard for our major fundraising event - LiftingSTAR2018

Bright Meadow KIDS Camp (BMK) and Youth Trail Pathway Camp (YTPC) are ministries of Larkfield Gospel Church that serve Ventura County children of abuse, abandonment and neglect living in foster care. We are looking for a postcard design to promote our single largest fundraising event of the year, NurturingSTAR2018, to raise awareness and support for children of abuse. NurturingSTAR is a dinner banquet on at an exclusive outdoor venue, "Willow Hollow" with a rustic, ranch feel and with spectacular panoramic views of the City of Camarillo. The event will include music, refreshments, appetizers, a Santa Maria-style barbeque (BBQ), coffee and dessert, testimonials from camp, prize drawings, an opportunity to partner with BMK and YTPC, and time to socialize before and after.
Updates

I have just uploaded text copy to help designers come closer to what we are looking for. Thank you very much for your interest! -Dale

Target Market(s)

People from both within and from outside our sponsoring church who have a heart for hurting children and who are willing and able to financially support our camping (BMK & YTPC) ministries.

Industry/Entity Type

Church

Font styles to use
Serif
Decorative
Script

Requirements
Must have
• Name: NurturingSTAR2018... raising awareness and support for children of abuse
• Date: Thursday, May 24, 2018, 6:30-8:00 pm
• Place: Willow Hollow at Marlowe Ranch, 7100 Quillan Road, Somis, California.
• Cost: $30 per person
• Tickets: Available at Ticketmill.example
• Front side should include the elements of the event (although not necessarily bulleted like below):
• • Social hour
• • Music
• • Hors d’eourves
• • Refreshments
• • Santa Maria-style BBQ dinner
• • Coffee & dessert
• • Prize drawings
• • Stories from camp
• See attachment for suggested copy for back side.
• BMK and YTPC logos should be included on the postcard. I’ve uploaded a variety of photos for the designer to choose from; they do not necessarily all have to be included. There are also lots more pics available on our Gatherbook (Bright Meadow KIDS of Ventura).
• The front-side of the postcard can be entirely images and text. The back-side of the post card should include our return address at the top left ("BMK/YTPC of Larkfield Gospel Church, 820 Fernbrook Lane, Ventura, CA 93003") and should leave at least the right half of the postcard clear for addressing and postage.
• BMK colors are purple (Pantone 267) and red (Pantone 186). YTPC colors are green and yellow.
Nice to have
• A selection of camp photos large enough to easily view, but no so many that they are too small to identify. And, perhaps, a design element that evokes a rustic, outdoors, western, ranch feel, but not so much that it seems that we are promoting a country hoedown.
Should not have
• Anything sexual or sensual, related to alcoholic beverages, gambling, guns, or anything negative.

```html
<!DOCTYPE html>
<html lang="en">
<head>
<meta charset="utf-8">
<title>NurturingSTAR 2018 Postcard</title>
<link rel="stylesheet" href="https://fonts.googleapis.com/css2?family=Monoton&family=Passion+One:wght@400;700&family=Roboto+Condensed:wght@300;400;700&family=Roboto:wght@400;500;700&family=Nothing+You+Could+Do&display=swap">
<style>
  :root {
    --page: #e6e6e6;
    --card-white: #ffffff;
    --night: #0d0d14;
    --tile-edge: #2a2a30;
    --camp-red: #e8141c;
    --camp-yellow: #ffd21a;
    --hot-orange: #ff5a0a;
    --pink: #f7a8c4;
    --ink: #1a1a1a;
    --navy: #2b2570;
    --sky: #1b93c7;
    --grass: #138a2c;
    --soft-white: #f2eef6;
  }
  html, body { margin: 0; padding: 0; width: 899px; height: 1200px; overflow: hidden; background: var(--page); }
  svg { display: block; }
  .headline { font-family: "Passion One", "Arial Black", sans-serif; }
  .cond { font-family: "Roboto Condensed", "Arial Narrow", sans-serif; }
  .body { font-family: "Roboto", Arial, sans-serif; }
  .display { font-family: "Monoton", "Impact", sans-serif; }
  .script { font-family: "Nothing You Could Do", cursive; }
  .front-tile { stroke: var(--tile-edge); stroke-width: 1; }
  .dark-tile { fill: #1c1c22; stroke: #2f2f36; }
  .bullet { fill: var(--hot-orange); }
  .feature { fill: var(--soft-white); font-size: 14.5px; font-weight: 300; }
  .rule { stroke: #a9a9b4; stroke-width: 1; }
</style>
</head>
<body>
<svg width="899" height="1200" viewBox="0 0 899 1200" xmlns="http://www.w3.org/2000/svg">
  <defs>
    <linearGradient id="panelGlow" x1="0" y1="0" x2="1" y2="1">
      <stop offset="0" stop-color="#d0214a"/>
      <stop offset="0.35" stop-color="#5a2a86"/>
      <stop offset="0.7" stop-color="#2c3f9a"/>
      <stop offset="1" stop-color="#4a1f5c"/>
    </linearGradient>
    <radialGradient id="panelBloom" cx="0.7" cy="0.75" r="0.6">
      <stop offset="0" stop-color="#38c0d8" stop-opacity="0.45"/>
      <stop offset="1" stop-color="#38c0d8" stop-opacity="0"/>
    </radialGradient>
    <linearGradient id="water" x1="0" y1="0" x2="0" y2="1"><stop offset="0" stop-color="#4fb7d6"/><stop offset="1" stop-color="#1e8fb8"/></linearGradient>
    <linearGradient id="forest" x1="0" y1="0" x2="0" y2="1"><stop offset="0" stop-color="#6d8a55"/><stop offset="1" stop-color="#8a7a5c"/></linearGradient>
    <linearGradient id="indoor" x1="0" y1="0" x2="0" y2="1"><stop offset="0" stop-color="#c99a7e"/><stop offset="1" stop-color="#2e5a3a"/></linearGradient>
    <linearGradient id="track" x1="0" y1="0" x2="0" y2="1"><stop offset="0" stop-color="#9ab07a"/><stop offset="1" stop-color="#b8624e"/></linearGradient>
    <filter id="cardShadow" x="-5%" y="-5%" width="110%" height="115%"><feDropShadow dx="0" dy="8" stdDeviation="8" flood-opacity="0.25"/></filter>
  </defs>

  <!-- FRONT -->
  <g class="postcard-front" filter="url(#cardShadow)">
    <rect x="76" y="45" width="764" height="495" fill="var(--night)"/>
  </g>
  <g class="front-collage">
    <rect class="dark-tile" x="283" y="60" width="22" height="22"/>
    <rect class="dark-tile" x="305" y="60" width="22" height="22"/>
    <rect class="dark-tile" x="330" y="85" width="22" height="22"/>
    <rect class="dark-tile" x="240" y="110" width="22" height="22"/>
    <rect class="dark-tile" x="380" y="60" width="22" height="22"/>
    <rect class="dark-tile" x="405" y="60" width="22" height="22"/>
    <rect class="dark-tile" x="380" y="194" width="22" height="22"/>
    <rect class="dark-tile" x="360" y="437" width="22" height="22"/>
    <rect class="dark-tile" x="284" y="390" width="22" height="22"/>
    <rect class="dark-tile" x="284" y="505" width="22" height="22"/>
    <rect class="front-tile" role="img" aria-label="Photo: boy at the edge of a camp swimming pool" x="88" y="59" width="118" height="160" fill="url(#water)"/>
    <rect class="front-tile" role="img" aria-label="Photo: camper on a log in the woods" x="210" y="59" width="61" height="64" fill="url(#forest)"/>
    <rect class="front-tile" role="img" aria-label="Photo: campers walking among pine trees" x="210" y="126" width="61" height="93" fill="url(#forest)"/>
    <rect class="front-tile" role="img" aria-label="Photo: camper riding a bicycle" x="274" y="138" width="78" height="81" fill="#7d8a6a"/>
    <rect class="front-tile" role="img" aria-label="Photo: camper on a climbing wall" x="302" y="85" width="50" height="50" fill="#9aa0a4"/>
    <rect class="front-tile" role="img" aria-label="Photo: campers on a trail ride" x="356" y="116" width="102" height="70" fill="#8aa070"/>
    <rect class="front-tile" role="img" aria-label="Photo: teens on a pool float" x="88" y="223" width="118" height="160" fill="url(#water)"/>
    <rect class="front-tile" role="img" aria-label="Photo: two girls in pink hats at a craft table" x="210" y="223" width="248" height="160" fill="url(#indoor)"/>
    <rect class="front-tile" role="img" aria-label="Photo: camper jumping into the pool" x="88" y="387" width="118" height="139" fill="#5aa7c4"/>
    <rect class="front-tile" role="img" aria-label="Photo: campers racing on a track" x="210" y="387" width="69" height="72" fill="url(#track)"/>
    <rect class="front-tile" role="img" aria-label="Photo: camper on a zip line" x="282" y="412" width="82" height="86" fill="#4c6a48"/>
    <rect class="front-tile" role="img" aria-label="Photo: campers in party hats" x="366" y="387" width="91" height="60" fill="#a88a62"/>
    <rect class="front-tile" role="img" aria-label="Photo: group of campers outside a lodge" x="366" y="451" width="91" height="72" fill="#6f8fa8"/>
  </g>

  <g class="front-panel">
    <rect x="472" y="45" width="368" height="495" fill="url(#panelGlow)"/>
    <rect x="472" y="45" width="368" height="495" fill="url(#panelBloom)"/>
    <line x1="472" y1="212" x2="840" y2="212" stroke="#ffffff" stroke-opacity="0.35"/>
    <line x1="472" y1="372" x2="840" y2="372" stroke="#ffffff" stroke-opacity="0.35"/>
    <text class="headline" x="656" y="88" text-anchor="middle" font-size="19" fill="var(--camp-red)">Bright Meadow KIDS Camp <tspan fill="#ffffff">&amp;</tspan></text>
    <text class="headline" x="656" y="112" text-anchor="middle" font-size="19" fill="var(--camp-yellow)">Youth Trail Pathway Camp</text>
    <text class="cond" x="656" y="138" text-anchor="middle" font-size="15" font-weight="300" fill="#ffffff">of Larkfield Gospel Church</text>
    <text class="cond" x="656" y="184" text-anchor="middle" font-size="15" font-weight="300" fill="#ffffff">invite you to join us for</text>
    <text class="display" x="525" y="272" font-size="46" fill="var(--hot-orange)" textLength="291" lengthAdjust="spacingAndGlyphs">NURTURING</text>
    <text class="display" x="525" y="353" font-size="74" fill="#ffffff" textLength="225" lengthAdjust="spacingAndGlyphs">STAR</text>
    <text class="display" x="760" y="314" font-size="36" fill="var(--pink)" textLength="54" lengthAdjust="spacingAndGlyphs">20</text>
    <text class="display" x="760" y="354" font-size="36" fill="var(--pink)" textLength="54" lengthAdjust="spacingAndGlyphs">18</text>
    <text class="script" x="658" y="403" text-anchor="middle" font-size="15" fill="#ffffff" textLength="326" lengthAdjust="spacingAndGlyphs">raising awareness &amp; support for children of abuse</text>
    <g class="feature-list cond">
      <circle class="bullet" cx="502" cy="440" r="4"/><text class="feature" x="514" y="445">Social hour</text>
      <circle class="bullet" cx="502" cy="463" r="4"/><text class="feature" x="514" y="468">Music</text>
      <circle class="bullet" cx="502" cy="486" r="4"/><text class="feature" x="514" y="491">Hors d’eourves</text>
      <circle class="bullet" cx="502" cy="509" r="4"/><text class="feature" x="514" y="514">Refreshments</text>
      <circle class="bullet" cx="630" cy="440" r="4"/><text class="feature" x="641" y="445">Santa Maria-style BBQ dinner</text>
      <circle class="bullet" cx="630" cy="463" r="4"/><text class="feature" x="641" y="468">Coffee &amp; dessert</text>
      <circle class="bullet" cx="630" cy="486" r="4"/><text class="feature" x="641" y="491">Prize drawings</text>
      <circle class="bullet" cx="630" cy="509" r="4"/><text class="feature" x="641" y="514">Stories from camp</text>
    </g>
  </g>

  <!-- BACK -->
  <g class="postcard-back" filter="url(#cardShadow)">
    <rect x="76" y="618" width="764" height="494" fill="var(--card-white)"/>
  </g>
  <g class="back-brands">
    <text class="body" x="168" y="678" font-size="14" font-weight="700" fill="var(--navy)">Bright Meadow KIDS</text>
    <circle cx="332" cy="672" r="22" fill="var(--grass)"/>
    <text class="body" x="362" y="678" font-size="14" font-weight="700" fill="var(--grass)">YTPC</text>
    <text class="cond" x="275" y="720" text-anchor="middle" font-size="14" font-weight="300" fill="var(--ink)">of Larkfield Gospel Church</text>
    <text class="cond" x="275" y="741" text-anchor="middle" font-size="13" font-weight="300" fill="var(--ink)">invite you to join us for</text>
  </g>
  <g class="back-title">
    <text class="display" x="144" y="790" font-size="40" fill="var(--camp-red)" textLength="268" lengthAdjust="spacingAndGlyphs">NURTURING</text>
    <text class="display" x="144" y="856" font-size="64" fill="var(--grass)" textLength="206" lengthAdjust="spacingAndGlyphs">STAR</text>
    <text class="display" x="361" y="823" font-size="32" fill="var(--sky)" textLength="49" lengthAdjust="spacingAndGlyphs">20</text>
    <text class="display" x="361" y="859" font-size="32" fill="var(--sky)" textLength="49" lengthAdjust="spacingAndGlyphs">18</text>
    <text class="script" x="278" y="880" text-anchor="middle" font-size="13" fill="var(--ink)" textLength="270" lengthAdjust="spacingAndGlyphs">raising awareness &amp; support for children of abuse</text>
  </g>
  <g class="back-details">
    <text class="cond" x="278" y="908" text-anchor="middle" font-size="12" font-weight="300" fill="var(--ink)">at the exclusive</text>
    <text class="body" x="278" y="928" text-anchor="middle" font-size="13" font-weight="700" fill="var(--sky)">WILLOW HOLLOW AT MARLOWE RANCH</text>
    <text class="body" x="278" y="944" text-anchor="middle" font-size="12" fill="var(--ink)">7100 Quillan Road, Somis, CA</text>
    <text class="body" x="192" y="960" font-size="12" fill="var(--ink)">on <tspan font-weight="700" fill="var(--camp-red)" dx="4">Thursday, May 24, 2018</tspan></text>
    <text class="body" x="278" y="976" text-anchor="middle" font-size="12" font-weight="700" fill="var(--camp-red)">6:30-8:00pm</text>
  </g>
  <g class="ticket-band">
    <rect x="76" y="987" width="396" height="53" fill="var(--grass)"/>
    <text class="body" x="274" y="1006" text-anchor="middle" font-size="10.5" fill="#ffffff">Tickets <tspan font-size="15" font-weight="700">$30</tspan> per person/Available at Ticketmill.example</text>
    <text class="body" x="274" y="1020" text-anchor="middle" font-size="10.5" fill="#ffffff">All proceeds to benefit BMKC &amp; YTPC serving children of abuse</text>
    <text class="body" x="274" y="1033" text-anchor="middle" font-size="10.5" fill="#ffffff">ages 7-14.</text>
  </g>
  <g class="contact-info cond">
    <text x="278" y="1060" text-anchor="middle" font-size="11.5" fill="var(--ink)">For more information:</text>
    <text x="278" y="1076" text-anchor="middle" font-size="11.5" fill="var(--ink)"><tspan font-weight="700" fill="var(--navy)">BMKC:</tspan> Director Dale Whitcombe <tspan font-weight="700" fill="var(--navy)">(805) 555-0142 / bmkcventura@example.net</tspan></text>
    <text x="278" y="1092" text-anchor="middle" font-size="11.5" fill="var(--ink)"><tspan font-weight="700" fill="var(--grass)">YTPC:</tspan> Director Theo Garand <tspan font-weight="700" fill="var(--grass)">(805) 555-0187 / theogarandphoto@example.com</tspan></text>
  </g>
  <rect class="base-stripe" x="76" y="1101" width="393" height="11" fill="var(--camp-red)"/>
  <g class="mailing-area">
    <rect x="738" y="640" width="79" height="92" rx="7" fill="none" stroke="#9a9aa2" stroke-width="1"/>
    <line class="rule" x1="546" y1="837" x2="813" y2="837"/>
    <line class="rule" x1="546" y1="874" x2="813" y2="874"/>
    <line class="rule" x1="546" y1="912" x2="813" y2="912"/>
  </g>
</svg>
</body>
</html>
```